Australian Lipstick Brand

We need packaging design for our tube for lipstick - the brand name is Vela. We are looking for a fun designs on the tube, integrating the logo.
The tube will be a frosted glass, and the lid black.
I will need the designs back in AI format.
I've attached a photo of an example - with our logo, but this is not want we are looking for. We are looking for something fun, but not too kiddy.
Updates
Hi Guys,
I have submitted a few images - the first image is kind of the design I would like something similar too (we are going for a candy theme) will still need the logo integrated.
The second picture is the picture of what the tube should look like. It is a tube (like a lipgloss/ lipstain)
Please email me if you have any further questions.
Thanks,
Marisa
Target Market(s)
Women aged between 16-35

```html
<!DOCTYPE html>
<html lang="en">
<head>
<meta charset="utf-8">
<title>Vela Lipstick – Tube Wrap</title>
<link rel="stylesheet" href="https://fonts.googleapis.com/css2?family=Great+Vibes&family=Josefin+Sans:wght@400&display=swap">
<style>
  :root {
    --canvas: #ffffff;
    --magenta: #ff14e6;
    --aqua: #9ffcf7;
    --doodle-light: #f3eefe;
    --doodle-violet: #c7a6f5;
    --doodle-pink: #f7b6ee;
    --doodle-cyan: #b5f1f4;
    --label-white: #ffffff;
  }
  html, body {
    margin: 0;
    padding: 0;
    width: 1200px;
    height: 1162px;
    overflow: hidden;
    background: var(--canvas);
  }
  .artboard {
    display: block;
    width: 1200px;
    height: 1162px;
  }
  .label-band {
    fill: var(--label-white);
    stroke: var(--magenta);
    stroke-width: 2;
  }
  .brand-name {
    font-family: "Great Vibes", cursive;
    fill: var(--magenta);
  }
  .product-type {
    font-family: "Josefin Sans", sans-serif;
    fill: var(--magenta);
  }
  .back-panel {
    fill: var(--aqua);
  }
</style>
</head>
<body>
<svg class="artboard" viewBox="0 0 1200 1162" xmlns="http://www.w3.org/2000/svg">
  <defs>
    <linearGradient id="doodle-tone" x1="0" y1="0" x2="1" y2="1">
      <stop offset="0" stop-color="var(--doodle-violet)"/>
      <stop offset="0.35" stop-color="var(--doodle-light)"/>
      <stop offset="0.65" stop-color="var(--doodle-pink)"/>
      <stop offset="1" stop-color="var(--doodle-cyan)"/>
    </linearGradient>
  </defs>

  <!-- Flat tube wrap: front -->
  <g class="wrap-front">
    <rect class="doodle-field" x="239" y="231" width="229" height="723" fill="url(#doodle-tone)"
          role="img" aria-label="Hand-drawn doodle pattern of hearts, flowers, stars and swirls on lined paper"/>
    <rect class="label-band" x="299" y="231" width="98" height="333"/>
    <text class="brand-name" font-size="88" text-anchor="middle"
          transform="translate(370 364) rotate(-90)">Vela</text>
    <text class="product-type" x="348" y="540" font-size="25" text-anchor="middle">Lipstick</text>
  </g>

  <!-- Flat tube wrap: back -->
  <rect class="back-panel" x="468" y="231" width="228" height="723"/>

  <!-- Tube preview -->
  <g class="tube-preview">
    <path class="doodle-field" d="M872 234 H1034 V631 Q1034 651 1014 651 H892 Q872 651 872 631 Z" fill="url(#doodle-tone)"
          role="img" aria-label="Doodle pattern of hearts, flowers and swirls wrapped around the tube"/>
    <rect class="label-band" x="909" y="234" width="80" height="272"/>
    <text class="brand-name" font-size="70" text-anchor="middle"
          transform="translate(966 345) rotate(-90)">Vela</text>
    <text class="product-type" x="950" y="488" font-size="21" text-anchor="middle">Lipstick</text>
  </g>
</svg>
</body>
</html>
```